Smart Proposal Template

I would like to create a reusable proposal template to be used for selling business to business products or services. Please see the attached word doc. The template must have expandable/contractable fields allowing the user to populate it with data without disrupting the format.. Please see the attached sample. The red font represents sample data for guiding the user in how to complete the template. This data must be able to be removed when the user ads in their actual data.

Target Market(s)

business owners

Font styles to use
Sans Serif

Colors
ec1f27
ffffff

Requirements
Must have
• template must be a tool that allows the users to fill in the blanks.
the red font that i have is text for suggesting how the users fill in the field.
The header must allow the user to replace my title with theirs.

```html
<!DOCTYPE html>
<html lang="en">
<head>
<meta charset="utf-8">
<title>Summitline – Smart Proposal Template</title>
<link href="https://fonts.googleapis.com/css2?family=Arimo:wght@400;700&family=Roboto+Condensed:wght@300;400&family=Open+Sans:wght@400&display=swap" rel="stylesheet">
<style>
:root{
  --backdrop:#e6e6e6;
  --paper:#f9f9f8;
  --ink:#1a1a1a;
  --guide:#e11f26;
  --brand:#d42030;
  --navy:#0f2233;
  --footer-band:#ececeb;
  --cover-dark:#0b0b0b;
  --rule:#444;
}
*{margin:0;padding:0;box-sizing:border-box}
html,body{width:1200px;height:542px;overflow:hidden;background:var(--backdrop)}
body{position:relative;font-family:"Arimo",Arial,sans-serif;color:var(--ink)}
.page{position:absolute;top:29px;width:339px;height:480px;background:var(--paper);overflow:hidden}
.page--cover{left:39px;background:radial-gradient(ellipse at 50% 0%,#2a2a2a 0%,var(--cover-dark) 60%)}
.page--intro{left:432px}
.page--schedule{left:826px}

/* cover */
.cover-mark{position:absolute;left:89.5px;top:85px;width:41.5px;height:45px;background:var(--brand)}
.cover-name{position:absolute;left:148px;top:100px;font-family:"Open Sans",sans-serif;font-size:11.5px;letter-spacing:1.3px;color:#fff}
.cover-title{position:absolute;left:0;width:100%;top:165px;text-align:center;font-family:"Roboto Condensed",sans-serif;font-weight:300;font-size:17px;line-height:30px;color:#fff}
.cover-date{position:absolute;left:0;width:100%;top:242px;text-align:center;font-family:"Open Sans",sans-serif;font-size:10px;color:#fff}
.cover-date sup{font-size:6px}
.cover-network{position:absolute;left:0;top:268px;width:100%;height:212px;background:linear-gradient(180deg,rgba(90,90,90,0) 0%,rgba(110,110,110,.35) 45%,rgba(60,60,60,.25) 100%)}

/* inner page chrome */
.top-band{position:absolute;left:0;top:0;width:100%;height:5px;background:var(--navy)}
.brand-mark{position:absolute;left:22px;top:17px;width:21px;height:22px;background:var(--brand)}
.brand-name{position:absolute;left:50px;top:25px;font-family:"Open Sans",sans-serif;font-size:5.8px;letter-spacing:.5px}
.contact{position:absolute;right:9px;top:25px;font-size:6.4px}
.page-footer{position:absolute;left:0;bottom:0;width:100%;height:46px;background:var(--footer-band);text-align:center;font-size:4.3px;line-height:6.4px;padding-top:7px}
.page-footer b{font-weight:700}
.page-footer a{color:var(--guide);font-weight:700}

/* content */
.block{position:absolute;left:22px;width:298px;font-size:6.3px;line-height:8.1px}
.heading{font-size:8.4px;font-weight:700;letter-spacing:.1px;line-height:10px}
.guide{color:var(--guide)}
.bullets{list-style:none}
.bullets li{position:relative;padding-left:11px}
.bullets li::before{content:"•";position:absolute;left:1px;color:var(--guide)}
.bullets--ink li::before{color:var(--ink)}
.arrows{list-style:none;padding-left:11px}
.arrows li{position:relative;padding-left:11px}
.arrows li::before{content:"➢";position:absolute;left:0;font-size:5.5px}

table{border-collapse:collapse;width:100%}
td,th{border:.6px solid var(--rule);vertical-align:top;text-align:left;font-size:6.3px;line-height:7.6px;padding:1px 3px}
th{font-weight:700}
.objectives td{height:84px}
.objectives .stake{vertical-align:middle}
.schedule tr{height:13px}
</style>
</head>
<body>

<section class="page page--cover">
  <div class="cover-mark"></div>
  <div class="cover-name">SUMMITLINE</div>
  <h1 class="cover-title">We help B2B Technology Companies<br>Penetrate New Markets &amp; Win Sales</h1>
  <p class="cover-date">March 21<sup>st</sup> 2020</p>
  <div class="cover-network" role="img" aria-label="Abstract connected-dots network graphic in grey tones"></div>
</section>

<section class="page page--intro">
  <div class="top-band"></div>
  <div class="brand-mark"></div>
  <div class="brand-name">SUMMITLINE</div>
  <div class="contact">800.555.0142 - summitlinesales.com</div>

  <div class="block" style="top:50px">
    <h2 class="heading">INTRODUCTION</h2>
    <p style="margin-top:4px">We have provided within this proposal a complete description of your solution including your Business Objectives, Alternate Strategies Considered, Solution Description, Deliverables, Schedule, Acceptance Criteria, Pricing, and our Unique Qualifications and Corporate Overview.</p>
  </div>

  <div class="block" style="top:100px">
    <h2 class="heading">YOUR BUSINESS OBJECTIVES</h2>
    <p style="margin-top:4px">After conversations and meetings with <span class="guide">insert names and titles for each business, user and financial level stakeholder</span>, we understand that <span class="guide">insert name of client organization</span> is requiring a solution that will meet the following Business Objectives:</p>
    <table class="objectives" style="margin-top:6px">
      <tr><th style="width:196px">BUSINESS OBJECTIVES</th><th>STAKEHOLDER/TITLE</th></tr>
      <tr>
        <td class="guide">Use the following list as a guideline for describing the clients Business Objectives as your understand them.
          <ul class="bullets">
            <li>Increase their sales, revenue, account penetration or market share</li>
            <li>Reduce work cycle time for delivering their solutions, servicing their customers, invoicing and collections.</li>
            <li>Improve their first-time quality and reduce waste.</li>
            <li>Meeting legal, regulatory, process, political or social compliance</li>
            <li>Increasing profit or reduce cost</li>
            <li>Increase corporate valuation or transferability</li>
          </ul>
        </td>
        <td class="stake guide">Insert corresponding<br>stakeholders name</td>
      </tr>
    </table>
  </div>

  <div class="block" style="top:258px">
    <h2 class="heading">ALTERNATE STRATEGIES CONSIDERED</h2>
    <ul class="bullets" style="margin-top:4px">
      <li>Take no action, return on investment is not justified - <span class="guide">Describe why the client must act now. Describe the ramifications of taking no action</span></li>
      <li>Utilize internal resources or providers - <span class="guide">Describe why this is not feasible. Internal resources have no track record of accomplishments or they are tied up with competing priorities</span></li>
      <li>Utilize competitive providers - <span class="guide">Provide a listing of qualified competitive providers that should be considered in addition to your organization.</span></li>
    </ul>
  </div>

  <div class="block" style="top:329px">
    <h2 class="heading">SOLUTION OVERVIEW</h2>
    <p style="margin-top:4px">We have developed a solution that aligns specifically to your Business Objectives as described above:</p>
    <ul class="arrows">
      <li>Functionality - <span class="guide">Describe your solution functionality and how it aligns to their Business Objectives</span></li>
      <li>Usability - <span class="guide">Describe the ease of operation for the end user or operator</span></li>
      <li>Reliability - <span class="guide">Describe the reliability of the solution within the specifics of the clients operating environment</span></li>
      <li>Graphic - <span class="guide">Insert a graphic depiction of the solution or product</span></li>
    </ul>
  </div>

  <footer class="page-footer">
    <b>Summitline - 800.555.0199 - <a>hello@summitline.example</a></b><br>
    All rights reserved. No part of this information may be reproduced or transmitted without the<br>
    expressed written permission of the authors. For further information contact: Summitline Inc.
  </footer>
</section>

<section class="page page--schedule">
  <div class="top-band"></div>
  <div class="brand-mark"></div>
  <div class="brand-name">SUMMITLINE</div>
  <div class="contact">800.555.0142 - summitlinesales.com</div>

  <div class="block" style="top:58px">
    <p>We anticipate the following schedule for the delivering our solution:</p>
  </div>

  <div class="block" style="top:75px;left:23px;width:292px">
    <table class="schedule">
      <tr><th style="width:42px">Schedule</th><th style="width:153px">Deliverable</th><th>Acceptance Criteria</th></tr>
      <tr style="height:17.7px"><td class="guide">Today</td><td class="guide">Contractual terms &amp; conditions</td><td class="guide">Define client acceptance criteria</td></tr>
      <tr style="height:14.4px"><td class="guide">Milestone 1</td><td class="guide">On time delivery</td><td></td></tr>
      <tr><td></td><td class="guide">Performance test completed</td><td></td></tr>
      <tr><td></td><td class="guide">Reliability review completed</td><td></td></tr>
      <tr style="height:15.4px"><td>Quarterly Reviews</td><td class="guide">Evaluation for obsolescence/technical or market change</td><td></td></tr>
      <tr style="height:11px"><td></td><td></td><td></td></tr>
    </table>
  </div>

  <div class="block" style="top:183px">
    <h2 class="heading">UNIQUELY QUALIFIED</h2>
    <ul class="bullets bullets--ink" style="margin-top:4px;line-height:7.6px">
      <li>Product/Service Superiority- Describe how this product or service is the best-fit solution for the clients specifics needs as you understand them to be</li>
      <li>Customization to need- Describe and list the specific customizations that enable best-fit</li>
      <li>Schedule/timing- Explain how you will ensure that this project will be completed or delivered as needed for the client to meet a schedule requirement</li>
      <li>Technical Alignment- <span class="guide">Explain how your solution aligns or integrates with the clients technical or installed technology environment</span></li>
      <li>Industry Alignment - <span class="guide">Define how your offering aligns with the needs of the clients industry.</span></li>
    </ul>
  </div>

  <div class="block" style="top:267px;line-height:8.8px">
    <p>CORPORATE OVERVIEW</p>
    <p class="guide">Insert 1 paragraph that describes your organization in terms of:</p>
    <p style="margin-top:8px">Skills that align to this specific solution</p>
    <p class="guide">Experience in delivering similar solutions</p>
    <p class="guide">Accomplishments of similar clients of projects</p>
  </div>

  <div class="block" style="top:328px">
    <h2 class="heading">PRICING</h2>
    <p style="margin-top:1px">Provide your full price. Pricing before any discounts.</p>
  </div>

  <footer class="page-footer">
    <b>Summitline - 800.555.0199 - <a>hello@summitline.example</a></b><br>
    All rights reserved. No part of this information may be reproduced or transmitted without the<br>
    expressed written permission of the authors. For further information contact: Summitline Inc.
  </footer>
</section>

</body>
</html>
```